Australian Accounting Firm Needs a Business Card Design

We need a business card design for a firm called QM Partners. We have a logo that we would like incorporated into the business card which i have attached to the brief. If possible we would like to incorporate the 'LB Registered Auditors' logo somewhere on the business card. If this doesn't suit perhaps instead of the logo you could put the words 'Chartered Accountant' in the same font as the words 'Taxation and Business Services'...
I have selected doubled sided however im more than happy to consider single sided designs as well. Whatever you think is suitable.
The information that needs to be included on the business card is as follows:

Marek Hollund B.Com CA
Director

Mobile: 0455 602 914

Email: marekh@qmpartners-example.com.au
Website: www.qmpartners-example.com.au

Address: 427 Wexford Lane
Kestrel Park VIC 3187
Postal Address: PO Box 875
Kestrel Park VIC 3187

We are looking for a sharp business card design, similar to the logo design. Keep in mind we are an accounting firm so nothing too crazy.

Thanks

```html
<!DOCTYPE html>
<html lang="en">
<head>
<meta charset="utf-8">
<title>QM Partners – Business Card</title>
<link href="https://fonts.googleapis.com/css2?family=Open+Sans:wght@300;400;600&family=Arimo:wght@400;700&display=swap" rel="stylesheet">
<style>
  :root {
    --ink: #0d0d0d;
    --card-black: #151515;
    --paper: #ffffff;
    --silver: #d9d7d2;
    --silver-dark: #a9a7a2;
    --mist: #e9e9e9;
    --light-text: #dcdcdc;
    --badge: #c9252c;
  }
  * { margin: 0; padding: 0; box-sizing: border-box; }
  html, body { width: 1139px; height: 1200px; overflow: hidden; }
  body { background: var(--mist); position: relative; font-family: "Open Sans", sans-serif; }

  .card {
    position: absolute; left: 120px; width: 900px; height: 514px;
    overflow: hidden; box-shadow: 0 10px 30px rgba(0,0,0,.25);
  }
  .card--front { top: 60px; }
  .card--back { top: 626px; background: var(--card-black); }

  .card__shapes { position: absolute; inset: 0; }

  .brand-name {
    font-family: "Open Sans", sans-serif; font-weight: 600;
    color: var(--light-text); letter-spacing: 1px; line-height: 1; white-space: nowrap;
  }
  .front-brand { position: absolute; left: 60px; top: 150px; }
  .front-brand .brand-name { font-size: 54px; }

  .services {
    font-family: "Open Sans", sans-serif; font-weight: 400;
    color: var(--light-text); text-transform: uppercase; line-height: 1.05; white-space: nowrap;
  }
  .front-services { position: absolute; left: 60px; top: 258px; font-size: 37px; }

  .accreditation {
    position: absolute; left: 150px; top: 393px;
    display: flex; align-items: center; gap: 12px;
  }
  .accreditation__seal {
    width: 44px; height: 44px; border-radius: 50%;
    background: var(--badge); border: 3px solid var(--paper);
  }
  .accreditation__label {
    font-family: "Arimo", sans-serif; font-weight: 700; font-size: 18px;
    color: var(--ink); line-height: 1.1;
  }

  .contact {
    position: absolute; left: 588px; top: 58px; width: 300px;
    font-family: "Arimo", sans-serif; color: var(--ink); white-space: nowrap;
  }
  .contact__name { font-size: 25px; font-weight: 700; }
  .contact__name small { font-size: 17px; font-weight: 400; }
  .contact__role { font-size: 20px; margin-left: 70px; margin-bottom: 32px; }
  .contact__list { list-style: none; }
  .contact__item { display: flex; align-items: flex-start; gap: 12px; font-size: 15.5px; font-weight: 700; margin-bottom: 12px; line-height: 1.3; }
  .contact__item--large { font-size: 20px; margin-top: 4px; }
  .contact__icon { width: 17px; height: 17px; flex: none; margin-top: 2px; }

  .back-lockup {
    position: absolute; left: 150px; top: 190px;
    display: flex; align-items: center;
  }
  .back-lockup .brand-name { font-size: 46px; }
  .back-lockup__rule { width: 2px; height: 150px; background: var(--light-text); margin: 0 30px; }
  .back-services { font-size: 29px; }
  .back-web { font-size: 16px; color: var(--light-text); margin-top: 22px; white-space: nowrap; }
</style>
</head>
<body>

<section class="card card--front">
  <svg class="card__shapes" viewBox="0 0 900 514" width="900" height="514">
    <rect width="900" height="514" fill="var(--card-black)"/>
    <rect x="0" y="375" width="600" height="62" fill="var(--silver)"/>
    <path d="M545 0 Q455 257 600 514 L900 514 L900 0 Z" fill="var(--paper)"/>
    <path d="M545 0 Q455 257 600 514 L585 514 Q470 257 560 0 Z" fill="var(--silver-dark)" transform="translate(-14 0)"/>
  </svg>

  <div class="front-brand"><span class="brand-name">QM PARTNERS</span></div>
  <p class="services front-services">Taxation and<br>Business Services</p>

  <div class="accreditation">
    <span class="accreditation__seal"></span>
    <span class="accreditation__label">Registered<br>Auditor</span>
  </div>

  <div class="contact">
    <p class="contact__name">Marek Hollund <small>(B.Com CA)</small></p>
    <p class="contact__role">Director</p>
    <ul class="contact__list">
      <li class="contact__item">
        <svg class="contact__icon" viewBox="0 0 18 18"><rect width="18" height="18" rx="3" fill="var(--ink)"/><rect x="5" y="3" width="8" height="12" rx="1.5" fill="none" stroke="#fff" stroke-width="1.5"/></svg>
        0455 602 914
      </li>
      <li class="contact__item">
        <svg class="contact__icon" viewBox="0 0 18 18"><rect x="1" y="3" width="16" height="12" fill="none" stroke="var(--ink)" stroke-width="1.6"/><path d="M1 3 L9 10 L17 3" fill="none" stroke="var(--ink)" stroke-width="1.6"/></svg>
        marekh@qmpartners-example.com.au
      </li>
      <li class="contact__item">
        <svg class="contact__icon" viewBox="0 0 18 18"><circle cx="9" cy="9" r="8" fill="var(--ink)"/><g fill="none" stroke="#fff" stroke-width="1"><circle cx="9" cy="9" r="5.5"/><ellipse cx="9" cy="9" rx="2.3" ry="5.5"/><path d="M3.5 9 H14.5"/></g></svg>
        www.qmpartners-example.com.au
      </li>
      <li class="contact__item">
        <svg class="contact__icon" viewBox="0 0 18 18"><rect width="18" height="18" rx="3" fill="var(--ink)"/><path d="M9 15 C5 10 5 8 5 7 A4 4 0 0 1 13 7 C13 8 13 10 9 15 Z" fill="#fff"/><circle cx="9" cy="7" r="1.6" fill="var(--ink)"/></svg>
        PO Box 875<br>Kestrel Park VIC 3187
      </li>
      <li class="contact__item contact__item--large">
        <svg class="contact__icon" viewBox="0 0 18 18"><rect width="18" height="18" rx="3" fill="var(--ink)"/><path d="M4 9 L9 4.5 L14 9 M5.5 8 V13.5 H12.5 V8" fill="none" stroke="#fff" stroke-width="1.4"/></svg>
        427 Wexford Lane<br>Kestrel Park VIC 3187
      </li>
    </ul>
  </div>
</section>

<section class="card card--back">
  <div class="back-lockup">
    <span class="brand-name">QM PARTNERS</span>
    <span class="back-lockup__rule"></span>
    <div>
      <p class="services back-services">Taxation and<br>Business Services</p>
      <p class="back-web">www.qmpartners-example.com.au</p>
    </div>
  </div>
</section>

</body>
</html>
```